Brenvick Holdings LLC, new Business cards

I'm moving offices and need new cards. Plus I'm open to modifying the current design of my card. I will keep the logo but would like to explore other layouts and fonts for the design. I've included the current double sided card for reference. I Like the navy color and white. Might be open to grays or silver. Needs to be clean and elegant.

Target Market(s)

Investors, buyers & sellers of private equities and real estate.

Contact Information for Business Card

Brenvick Holdings
Dorian P.K. Halvers, Managing Principal
418 Ostrander Ave., Suite 612
Denver, CO 80319
M: 970-555-0147, O: 303-555-0192
Dorian@brenvickholdings.example
Brenvickholdings.example

Colors
0354a2
ffffff
c4c4c4

Requirements
Must have
• Business card details.
• Logo raised or embossed, it was designed after a wax seal. Current has raised ink.
Nice to have
• Space on card to write additional notes.

```html
<!DOCTYPE html>
<html lang="en">
<head>
<meta charset="utf-8">
<title>Brenvick Holdings – Business Cards</title>
<link href="https://fonts.googleapis.com/css2?family=Open+Sans:wght@400;600;700&display=swap" rel="stylesheet">
<style>
  :root {
    --navy: #0354a2;
    --navy-deep: #0a4a92;
    --white: #ffffff;
    --silver: #c4c4c4;
    --ink: #555a60;
    --backdrop: #ebebeb;
  }
  * { box-sizing: border-box; margin: 0; padding: 0; }
  html, body {
    width: 1200px; height: 1200px; overflow: hidden;
    background: var(--backdrop);
    font-family: "Open Sans", Arial, sans-serif;
  }
  .canvas { position: relative; width: 1200px; height: 1200px; }

  .card {
    position: absolute;
    width: 770px; height: 440px;
    overflow: hidden;
    box-shadow: 0 2px 6px rgba(0,0,0,0.12);
  }

  /* Front side */
  .card-front { left: 70px; top: 110px; background: var(--navy); }
  .card-front .tagline {
    position: absolute; left: 0; right: 0; top: 200px;
    text-align: center; color: var(--white);
    font-size: 19px; letter-spacing: 0.5px; font-weight: 400;
  }
  .card-front .seal-mark {
    position: absolute; left: -90px; bottom: -130px;
    width: 360px; height: 360px; border-radius: 50%;
    background: var(--navy-deep);
  }
  .card-front .seal-name {
    position: absolute; left: 30px; bottom: 62px;
    color: var(--white); opacity: 0.18;
    font-size: 16px; font-weight: 600; letter-spacing: 2px;
  }

  /* Back side */
  .card-back { left: 360px; top: 650px; background: var(--white); }
  .card-back .seal-mark {
    position: absolute; right: -120px; top: -130px;
    width: 360px; height: 360px; border-radius: 50%;
    background: var(--navy);
  }
  .card-back .brand-name {
    position: absolute; right: 270px; top: 40px;
    color: var(--navy); font-size: 18px; font-weight: 600; letter-spacing: 3px;
  }
  .contact { position: absolute; left: 58px; top: 170px; color: var(--ink); }
  .contact .person-name { color: var(--navy); font-size: 26px; font-weight: 700; line-height: 1.1; }
  .contact .person-title { font-size: 17px; margin-top: 2px; }
  .contact .divider { width: 32px; height: 5px; background: var(--navy); margin: 18px 0 18px; }
  .contact .address { font-size: 17px; line-height: 1.35; margin-bottom: 14px; }
  .contact .lines { list-style: none; font-size: 17px; line-height: 1.35; }
  .contact .lines li { display: flex; align-items: center; gap: 8px; }
  .contact .lines svg { width: 15px; height: 15px; flex: none; }
</style>
</head>
<body>
<div class="canvas">

  <section class="card card-front" aria-label="Card front">
    <div class="seal-mark" role="img" aria-label="Embossed wax seal emblem"></div>
    <span class="seal-name">BRENVICK HOLDINGS</span>
    <p class="tagline">FAMILY OFFICE INVESTMENT FIRM</p>
  </section>

  <section class="card card-back" aria-label="Card back">
    <div class="seal-mark" role="img" aria-label="Wax seal emblem"></div>
    <span class="brand-name">BRENVICK HOLDINGS</span>
    <div class="contact">
      <p class="person-name">Dorian P.K. Halvers</p>
      <p class="person-title">Managing Principal</p>
      <div class="divider"></div>
      <p class="address">418 Ostrander Ave., Suite 612<br>Denver, CO 80319</p>
      <ul class="lines">
        <li>
          <svg viewBox="0 0 16 16" aria-hidden="true"><rect x="4" y="1" width="8" height="14" rx="1.5" fill="none" stroke="#0354a2" stroke-width="1.5"/><line x1="7" y1="12.5" x2="9" y2="12.5" stroke="#0354a2" stroke-width="1.5"/></svg>
          970.555.0147
        </li>
        <li>
          <svg viewBox="0 0 16 16" aria-hidden="true"><path d="M3 2l3 0 1 3.5-2 1.2a8 8 0 0 0 4.3 4.3l1.2-2 3.5 1v3c0 .6-.4 1-1 1A12 12 0 0 1 2 3c0-.6.4-1 1-1z" fill="#0354a2"/></svg>
          303.555.0192
        </li>
        <li>
          <svg viewBox="0 0 16 16" aria-hidden="true"><rect x="1" y="3" width="14" height="10" fill="none" stroke="#0354a2" stroke-width="1.5"/><path d="M1 3l7 6 7-6M1 13l5-5M15 13l-5-5" fill="none" stroke="#0354a2" stroke-width="1.3"/></svg>
          dorian@brenvickholdings.example
        </li>
        <li>
          <svg viewBox="0 0 16 16" aria-hidden="true"><circle cx="8" cy="8" r="6.5" fill="none" stroke="#0354a2" stroke-width="1.4"/><ellipse cx="8" cy="8" rx="3" ry="6.5" fill="none" stroke="#0354a2" stroke-width="1.2"/><line x1="1.5" y1="8" x2="14.5" y2="8" stroke="#0354a2" stroke-width="1.2"/></svg>
          brenvickholdings.example
        </li>
      </ul>
    </div>
  </section>

</div>
</body>
</html>
```